Signs to Go on the Side of Shipping Containers

We are a startup in North Alabama that will lease/sale shipping containers as Portable Storage options for business/construction sites. We need signs that will be mass produced and be mounted on every side of the container for advertising/visibility.
We need multiple sizes depending on the side the sign will be on/ the size of the container it is being mounted on.
Website: www.brindlecrestboxes.com

MUST BE SIMPLE AND EASY TO READ. Not to Busy. See example in
Updates

One designer is asking me to extend deadline. This is my first design project so not sure why they want me to do this but figured I would.

Target Market(s)

Business owners/Construction Companies/Individuals Moving

Industry/Entity Type

Portable Storage

Colors
0054AA
0677BA
7BADD7
CADEEF
E8F1F8

Requirements
Must have
• Company Name(Brindle Crest Boxes)/Phone Number (256-489-3172)/Website (www.brindlecrestboxes.com
Nice to have
• Play on the container shapes/pattern.

```html
<!DOCTYPE html>
<html lang="en">
<head>
<meta charset="utf-8">
<title>Brindle Crest Boxes – Container Sign</title>
<link rel="stylesheet" href="https://fonts.googleapis.com/css2?family=Anton&family=Montserrat:wght@800;900&family=Roboto+Condensed:wght@700&display=swap">
<style>
  :root {
    --page: #231f20;
    --navy: #0054AA;
    --brand-blue: #0677BA;
    --sky: #7BADD7;
    --panel: #8bbfec;
    --ice: #CADEEF;
    --mist: #E8F1F8;
    --ink: #000000;
    --white: #ffffff;
  }
  * { box-sizing: border-box; margin: 0; padding: 0; }
  html, body { width: 1200px; height: 1200px; overflow: hidden; background: var(--page); }
  .sign {
    position: absolute; left: 47px; top: 323px; width: 1107px; height: 553px;
    background: linear-gradient(90deg, var(--panel) 0%, var(--panel) 55%, #a9d0f2 68%, #cfe3f5 82%, #d6e8f8 100%);
    overflow: hidden;
  }
  .photo-stack {
    position: absolute; left: 704px; top: 0; width: 403px; height: 477px;
    background: linear-gradient(180deg, #3f8fde 0%, #2f7fd0 55%, #4a92d6 100%);
    -webkit-mask-image: linear-gradient(90deg, transparent 0%, #000 40%);
    mask-image: linear-gradient(90deg, transparent 0%, #000 40%);
  }
  .photo-unit {
    position: absolute; left: 23px; top: 87px; width: 225px; height: 208px;
    background: linear-gradient(135deg, #2c7fc2 0%, #1f6aa8 60%, #175b93 100%);
  }
  .title {
    position: absolute; left: 198px; width: 700px; text-align: center; line-height: 1;
  }
  .title-top {
    top: 92px; font-family: "Montserrat", sans-serif; font-weight: 900;
    font-size: 54px; color: var(--ink);
  }
  .title-main {
    top: 150px; font-family: "Anton", sans-serif; font-weight: 400;
    font-size: 102px; letter-spacing: 2px; color: var(--brand-blue);
  }
  .tagline {
    position: absolute; left: 198px; width: 700px; top: 258px; text-align: center; line-height: 1;
    font-family: "Montserrat", sans-serif; font-weight: 800; font-size: 28px;
    letter-spacing: 10px; padding-left: 10px; color: var(--ink);
  }
  .offer {
    position: absolute; left: 0; top: 329px; width: 809px; height: 62px;
    background: var(--ink); border-radius: 0 31px 31px 0;
    display: flex; align-items: center; padding-left: 36px;
    font-family: "Roboto Condensed", sans-serif; font-weight: 700; font-size: 47px;
    color: var(--ice); white-space: nowrap;
  }
  .contact-bar {
    position: absolute; left: 0; bottom: 0; width: 100%; height: 76px;
    background: var(--brand-blue); display: flex; align-items: center;
    font-family: "Roboto Condensed", sans-serif; font-weight: 700; font-size: 54px;
    color: var(--white); white-space: nowrap;
  }
  .contact-item { display: flex; align-items: center; gap: 8px; }
  .contact-phone { margin-left: 26px; }
  .contact-web { margin-left: 22px; }
  .contact-icon { width: 40px; height: 40px; flex: none; }
</style>
</head>
<body>
  <main class="sign">
    <div class="photo-stack" role="img" aria-label="Photo of stacked blue shipping containers against the sky"></div>
    <div class="photo-unit" role="img" aria-label="Photo of a blue shipping container carrying the company name"></div>

    <h1 class="title title-top">BRINDLE CREST</h1>
    <p class="title title-main">BOXES</p>
    <p class="tagline">SALES &amp; RENTALS</p>

    <p class="offer">BUY OR RENT SHIPPING CONTAINERS</p>

    <footer class="contact-bar">
      <div class="contact-item contact-phone">
        <svg class="contact-icon" viewBox="0 0 40 40" fill="none" stroke="#CADEEF" stroke-width="2.5" stroke-linecap="round" stroke-linejoin="round" aria-hidden="true">
          <path d="M9 5l6 8-3 4c2 5 5 8 10 11l4-3 8 6-4 5C17 36 4 23 4 9z"/>
          <path d="M22 8a10 10 0 0 1 10 10"/>
          <path d="M22 3a15 15 0 0 1 15 15"/>
        </svg>
        <span>256-489-3172</span>
      </div>
      <div class="contact-item contact-web">
        <svg class="contact-icon" viewBox="0 0 40 40" fill="none" stroke="#CADEEF" stroke-width="2.2" aria-hidden="true">
          <circle cx="19" cy="19" r="15"/>
          <ellipse cx="19" cy="19" rx="7" ry="15"/>
          <path d="M4 19h30M7 11h24M7 27h24M19 4v30"/>
          <path d="M27 25l10 5-4 1 3 5-2 1-3-5-3 3z" fill="#CADEEF" stroke="none"/>
        </svg>
        <span>www.brindlecrestboxes.com</span>
      </div>
    </footer>
  </main>
</body>
</html>
```